Business Cards Needed for Innovative Healthcare Marketing Company

We are a marketing company focused on healthcare. Our company is all about rebranding yourself renewing your image and generating results. The phoenix stands for "reborn" or "rising" which we provide new brands for our clients we take their old brands and renew it with creativity and innovation. I am looking for a business card with color dimension. I have attached an example of a card I think has the look and feel of what I am trying to accomplish. I like that the card example has black and grey font colors, I like the font placement and the small logo, I really like the use of the colors on the right those are the colors of my logo. My logo is phoenix so maybe incorporating flames similar to that design. I would like the back a solid color maybe red with an opaque version of the logo and website. As a marketing company I am always open to creative liberty!

Target Market(s)

Doctors and business professionals.

Industry/Entity Type

Marketing

Contact Information for Business Card

Velmora Health Care Marketing
Dana Prewitt- CEO
#(407)555-0172
email-dana@velmora.com
website- velmora.com

Font styles to use
Sans Serif

Colors
ec1f27
f37122
ffc214
fbed22
fbf289
f04a50

Requirements
Must have
• The logo and required information
Nice to have
• icons by the information
Should not have
• child like font

```html
<!DOCTYPE html>
<html lang="en">
<head>
<meta charset="utf-8">
<title>Velmora Health Care Marketing – Business Card</title>
<link href="https://fonts.googleapis.com/css2?family=Raleway:wght@300;400&family=Roboto+Slab:wght@400;700&display=swap" rel="stylesheet">
<style>
  :root {
    --bg: #e8e5e1;
    --paper: #ffffff;
    --brand-red: #a83326;
    --accent-red: #c0392b;
    --flame-yellow: #ffc214;
    --ghost-grey: #dcdcdc;
    --text-grey: #8a8a8a;
    --soft-grey: #b9b9bd;
  }
  * { box-sizing: border-box; margin: 0; padding: 0; }
  html, body { width: 1200px; height: 913px; overflow: hidden; }
  body { background: var(--bg); position: relative; font-family: "Raleway", sans-serif; }

  .card {
    position: absolute;
    width: 520px;
    height: 297px;
    background: var(--paper);
    overflow: hidden;
    box-shadow: 0 6px 18px rgba(0,0,0,0.18);
  }
  .card--back { left: 60px; top: 150px; }
  .card--front { left: 620px; top: 466px; }

  /* Back */
  .back-emblem {
    position: absolute; left: 52px; top: 78px;
    width: 140px; height: 140px; border-radius: 50%;
    background: #f1f1f2;
  }
  .back-brand { position: absolute; left: 215px; top: 92px; width: 270px; }
  .back-brand__name {
    font-weight: 300; font-size: 48px; letter-spacing: 2px;
    color: var(--ghost-grey); line-height: 1;
  }
  .back-brand__rule { height: 1px; background: var(--ghost-grey); margin: 6px 0 4px; }
  .back-brand__tagline {
    font-weight: 300; font-size: 11px; letter-spacing: 1.5px;
    color: var(--ghost-grey); text-transform: uppercase;
  }
  .back-url {
    position: absolute; left: 300px; top: 200px;
    font-family: "Roboto Slab", serif; font-size: 18px; color: var(--text-grey);
  }
  .back-url strong { color: var(--accent-red); font-weight: 700; }

  /* Front */
  .front-shapes { position: absolute; inset: 0; }
  .front-brand { position: absolute; left: 34px; top: 110px; width: 180px; }
  .front-brand__mark {
    display: block; width: 14px; height: 14px; border-radius: 50%;
    background: var(--flame-yellow); margin-bottom: 10px;
  }
  .front-brand__name {
    font-weight: 400; font-size: 32px; letter-spacing: 1px;
    color: var(--brand-red); line-height: 1;
  }
  .front-brand__rule { height: 1px; background: var(--brand-red); margin: 5px 0 3px; }
  .front-brand__tagline {
    font-size: 8px; letter-spacing: 1px; color: var(--brand-red); text-transform: uppercase;
  }
  .contact { position: absolute; left: 332px; top: 80px; color: #fff; }
  .contact__name { font-family: "Roboto Slab", serif; font-size: 20px; font-weight: 400; }
  .contact__name b { font-weight: 700; }
  .contact__role { font-family: "Roboto Slab", serif; font-size: 12px; color: var(--soft-grey); margin-bottom: 12px; }
  .contact__list { list-style: none; }
  .contact__item {
    display: flex; align-items: center; gap: 8px;
    font-family: "Roboto Slab", serif; font-size: 12px; margin-bottom: 6px;
  }
  .contact__icon {
    width: 16px; height: 16px; border-radius: 50%; background: #fff;
    display: flex; align-items: center; justify-content: center; flex: none;
  }
</style>
</head>
<body>

<section class="card card--back" aria-label="Card back">
  <div class="back-emblem"></div>
  <div class="back-brand">
    <div class="back-brand__name">VELMORA</div>
    <div class="back-brand__rule"></div>
    <div class="back-brand__tagline">Healthcare Marketing</div>
  </div>
  <div class="back-url">www.<strong>velmora</strong>.com</div>
</section>

<section class="card card--front" aria-label="Card front">
  <svg class="front-shapes" width="520" height="297" viewBox="0 0 520 297" aria-hidden="true">
    <path d="M200 0 H238 C300 80 330 190 340 297 H334 C318 190 282 80 200 0 Z" fill="var(--flame-yellow)"/>
    <path d="M245 0 H520 V297 H348 C338 190 308 80 245 0 Z" fill="var(--brand-red)"/>
  </svg>

  <div class="front-brand">
    <span class="front-brand__mark"></span>
    <div class="front-brand__name">VELMORA</div>
    <div class="front-brand__rule"></div>
    <div class="front-brand__tagline">Healthcare Marketing</div>
  </div>

  <div class="contact">
    <div class="contact__name">Dana <b>PREWITT</b></div>
    <div class="contact__role">CEO</div>
    <ul class="contact__list">
      <li class="contact__item">
        <span class="contact__icon">
          <svg width="10" height="10" viewBox="0 0 24 24"><path fill="#a83326" d="M6.6 10.8a15 15 0 0 0 6.6 6.6l2.2-2.2c.3-.3.7-.4 1-.2 1.1.4 2.3.6 3.6.6.6 0 1 .4 1 1V20c0 .6-.4 1-1 1A17 17 0 0 1 3 4c0-.6.4-1 1-1h3.5c.6 0 1 .4 1 1 0 1.3.2 2.5.6 3.6.1.3 0 .7-.2 1z"/></svg>
        </span>(407) 555-0172
      </li>
      <li class="contact__item">
        <span class="contact__icon">
          <svg width="10" height="10" viewBox="0 0 24 24"><path fill="#a83326" d="M2 5h20v14H2z"/><path fill="none" stroke="#fff" stroke-width="2" d="M2 6l10 7 10-7"/></svg>
        </span>dana@velmora.com
      </li>
      <li class="contact__item">
        <span class="contact__icon">
          <svg width="10" height="10" viewBox="0 0 24 24"><g fill="none" stroke="#a83326" stroke-width="2.4"><circle cx="12" cy="12" r="9"/><path d="M3 12h18M12 3c3 3 3 15 0 18M12 3c-3 3-3 15 0 18"/></g></svg>
        </span>velmora.com
      </li>
    </ul>
  </div>
</section>

</body>
</html>
```